Craft oriented film company needs a Business Card design

Hi all,
We're a 2-man band film company in New Zealand called Kestrel Pictures. We're good honest blokes, who are very passionate about the craft of film making. I've attached our current logo which has a bit of a crafty/artisan feel that we like. Feel free to use it - or throw the baby out with the bathwater and start again..... you never know, you might inspire a complete brand re-work.

In any case, the vibe we want to give out is that we are solid, dependable and no bullshit - but without compromising creative excellence and being in the now. We like the 'Brooklyn' artisan style of work.

Preferably single sided.

We need the standard stuff:
Name, job title, cellphone, email address and physical address (this can be smaller if you like - street, suburb, city & zip, country [if you want])

Check out our website to learn more about us: kestrelpictures.example

Target Market(s)

Brand marketers and advertising agency creatives looking for video production.

Industry/Entity Type

Baby

Requirements
Should not have
• Nothing flashy or too 'futuristic', we want it to feel grounded and real. A limited colour palette is preferred.
We don't want any film reels or cameras or anything obvious like that.

```html
<!DOCTYPE html>
<html lang="en">
<head>
<meta charset="utf-8">
<title>Kestrel Pictures — Business Card</title>
<link rel="stylesheet" href="https://fonts.googleapis.com/css2?family=Oswald:wght@400;600&display=swap">
<style>
  :root {
    --backdrop: #d3d3d3;
    --card-light: #ffffff;
    --card-dark: #4a4446;
    --ink: #111111;
    --ink-soft: #2a2a2a;
    --paper-text: #ffffff;
    --ghost: #ededed;
    --icon-bg: #8a8a8a;
  }
  * { margin: 0; padding: 0; box-sizing: border-box; }
  html, body {
    width: 1200px; height: 800px; overflow: hidden;
    background: var(--backdrop);
    font-family: "Oswald", "Arial Narrow", sans-serif;
  }
  .stage {
    position: relative; width: 1200px; height: 800px;
    display: flex; align-items: center; justify-content: center; gap: 60px;
  }
  .card {
    position: relative; width: 500px; height: 286px;
    border-radius: 12px; overflow: hidden;
  }
  .card--front { background: var(--card-light); }
  .card--back { background: var(--card-dark); }

  .brand {
    position: absolute; display: flex; align-items: center; gap: 14px;
    text-transform: uppercase; font-weight: 600; line-height: 0.95;
  }
  .brand__dot { flex: none; width: 22px; height: 22px; border-radius: 50%; }
  .brand__name { font-size: 40px; letter-spacing: 1px; }

  .card--front .brand { left: 34px; top: 92px; color: var(--ink); }
  .card--front .brand__dot { background: var(--ink); }

  .ghost-name {
    position: absolute; right: -30px; top: 70px;
    font-size: 120px; font-weight: 600; color: var(--ghost);
    text-transform: uppercase; letter-spacing: 2px; line-height: 1;
  }

  .contact {
    position: absolute; right: 34px; top: 58px; text-align: right;
    text-transform: uppercase; color: var(--ink-soft);
  }
  .contact__name { font-size: 24px; font-weight: 600; letter-spacing: 2px; color: var(--ink); line-height: 1.05; }
  .contact__role { font-size: 14px; letter-spacing: 3px; margin-bottom: 18px; }
  .contact__line {
    display: flex; justify-content: flex-end; align-items: center; gap: 8px;
    font-size: 12px; letter-spacing: 1px; line-height: 1.6;
  }
  .contact__icon {
    width: 14px; height: 14px; border-radius: 50%; background: var(--icon-bg);
    display: inline-flex; align-items: center; justify-content: center;
  }
  .contact__line--plain { padding-right: 22px; }

  .card--back .brand {
    left: 50%; top: 50%; transform: translate(-50%, -58%);
    color: var(--paper-text); flex-direction: row;
  }
  .card--back .brand__dot { background: var(--paper-text); }
  .back__url {
    position: absolute; left: 0; right: 0; bottom: 40px; text-align: center;
    color: var(--paper-text); font-size: 12px; font-weight: 600;
    letter-spacing: 1.5px; text-transform: uppercase;
  }
</style>
</head>
<body>
<main class="stage">
  <section class="card card--front" aria-label="Card front">
    <div class="ghost-name" aria-hidden="true">Kestrel</div>
    <div class="brand">
      <span class="brand__dot"></span>
      <span class="brand__name">Kestrel<br>Pictures</span>
    </div>
    <div class="contact">
      <p class="contact__name">Tom Harland</p>
      <p class="contact__role">Manager</p>
      <p class="contact__line">0215550198
        <span class="contact__icon"><svg width="8" height="8" viewBox="0 0 10 10"><path d="M2 1h2l1 2.5-1.3 1a5 5 0 0 0 2 2l1-1.3L9 6.5v2A1 1 0 0 1 8 9.5 7.5 7.5 0 0 1 1 2a1 1 0 0 1 1-1z" fill="#fff"/></svg></span>
      </p>
      <p class="contact__line">info@kestrelpictures.example
        <span class="contact__icon"><svg width="8" height="8" viewBox="0 0 10 10"><rect x="1" y="2.5" width="8" height="5.5" fill="none" stroke="#fff" stroke-width="1"/><path d="M1 2.5l4 3 4-3" fill="none" stroke="#fff" stroke-width="1"/></svg></span>
      </p>
      <p class="contact__line">#1408B
        <span class="contact__icon"><svg width="8" height="8" viewBox="0 0 10 10"><path d="M5 9.5S1.8 6 1.8 4a3.2 3.2 0 0 1 6.4 0C8.2 6 5 9.5 5 9.5z" fill="#fff"/><circle cx="5" cy="4" r="1.1" fill="#8a8a8a"/></svg></span>
      </p>
      <p class="contact__line contact__line--plain">Harbour Lane</p>
      <p class="contact__line contact__line--plain">Grey Lynn</p>
      <p class="contact__line contact__line--plain">Auckland</p>
    </div>
  </section>

  <section class="card card--back" aria-label="Card back">
    <div class="brand">
      <span class="brand__dot"></span>
      <span class="brand__name">Kestrel<br>Pictures</span>
    </div>
    <p class="back__url">www.kestrelpictures.example</p>
  </section>
</main>
</body>
</html>
```